Design "RIDGEMANTIS" Shopify online store for hunting, outdoor and tactical accessories, appare

Design and setup Shopify platform online store for hunting, outdoor and tactical accessories, apparel.

Logo has been uploaded. Snapgrid, Campfeed and domain all setuop

A really modern easy to navigate online store that I can add and remove categories, add and remove products, update images, slider images, must have a AUD, USD, EUR, NZD and GBP currency converter drop down. RRPs will start in AUD. domain name is already registered and logo is done. Products are being photographed in readiness for you to set up the site. Fast shopping cart as guest with just name and address vs joining and collecting info for newsletters. Ability to send out newsletters. Home page that showcases 4-6 key categories of the site with hero images that can be updated by me. A clear navigation pane across the top. In the shopping part a clear categories navigation that can be updated as required. Free postage Australia and NZ, international shipment extra. Ultimately I need a great design as we have great products appealing to hunters, people who love the outdoors from camping to hiking, to tactical supplies. It's important to be strong website that shows quality and is easy to get arouund. Most of all it is brand new so whatever you can do to help drive traffic to it please do so. I will be managing it when ready with view to hiring a social media/web analyst to support me in a month.

Target Market(s)

Australian hunters and outdoor lovers - camping, hiking, motorbikes (dirt bikes / MX), and tactical professionals

Industry/Entity Type

Online Shopping

Coding

Coded - Design and coding required

Number of Pages Required

5+ page

Requirements
Must have
• As per my description plus up to the designers. You are the experts. I want it to look great but ultimately it has to get traffic and SELL PRODUCT
• Would like option for people to review products, eg leave 1-5 stars.
• After pay and Paywell for payment is my suggestion but I'm not the expert
• Work on computers, tablets and smartphones - compatible for all devices
Nice to have
• Product thumbnails, rankings. Can click on product to see more pictures, video and details. Size charts for apparel.
• Products will be things such as bags, equipment, accessories, clothing - all designed for outdoor activities predominantly hunting, camping, MX dirt bike riding, fishing, etc

```html
<!DOCTYPE html>
<html lang="en">
<head>
<meta charset="utf-8">
<title>RIDGEMANTIS – Hunting, Outdoor &amp; Tactical</title>
<link href="https://fonts.googleapis.com/css2?family=Montserrat:wght@500;600;700;800&family=Open+Sans:wght@400;600&display=swap" rel="stylesheet">
<style>
:root{
  --orange:#ff6a00;
  --black:#000;
  --nav:#151515;
  --dark-text:#111;
  --muted:#8a8a8a;
  --light-bg:#f4f4f4;
  --line:#e2e2e2;
  --teal:#1fbc98;
  --star:#f5b400;
  --star-off:#d0d0d0;
  --white:#fff;
}
*{margin:0;padding:0;box-sizing:border-box}
html,body{width:1200px;height:2560px;overflow:hidden}
body{font-family:"Open Sans",Arial,sans-serif;color:var(--dark-text);background:var(--white);position:relative}
.heading{font-family:"Montserrat",Arial,sans-serif}
a{color:inherit;text-decoration:none}
.icon-defs{position:absolute;width:0;height:0}

/* top bar */
.top-bar{height:34px;background:var(--black);color:var(--white);font-size:12px;display:flex;justify-content:flex-end;align-items:center;gap:26px;padding-right:111px}
.top-bar .currency b{font-weight:600}

/* header */
.site-header{height:89px;background:var(--black);position:relative}
.brand{position:absolute;left:50%;top:24px;transform:translateX(-50%);font-family:"Montserrat",Arial,sans-serif;font-weight:800;font-size:30px;color:var(--orange);letter-spacing:1px;display:flex;align-items:center;gap:10px}
.brand .mark{width:16px;height:16px;background:var(--orange)}
.cart-box{position:absolute;right:111px;top:17px;width:112px;height:48px;border:1px solid #444;padding:7px 10px;color:#ccc;font-size:11px}
.cart-box .total{color:var(--orange);font-size:14px;font-weight:600;display:block;margin-top:2px}
.cart-box svg{position:absolute;right:9px;top:13px}

/* nav */
.main-nav{height:43px;background:var(--nav);display:flex;justify-content:center;align-items:center;gap:38px;font-family:"Montserrat",Arial,sans-serif;font-size:12px;font-weight:600;color:var(--white)}

/* hero */
.hero{height:514px;position:relative;overflow:hidden}
.hero-photo{position:absolute;inset:0;
  background:
    linear-gradient(90deg,rgba(0,0,0,0) 0%,rgba(0,0,0,0) 40%,rgba(22,24,16,.78) 55%,rgba(22,24,16,.7) 66%,rgba(0,0,0,.15) 80%,rgba(0,0,0,.35) 100%),
    linear-gradient(180deg,#101426 0%,#2d1c2c 22%,#7a3220 40%,#d9661c 50%,#a8451a 56%,#2a1a10 66%,#0e0d09 100%);}
.hero-copy{position:absolute;left:111px;top:222px;color:var(--white)}
.hero-title{font-weight:700;font-size:36px;line-height:1.05;text-transform:uppercase}
.hero-title span{display:block;margin-left:162px}
.hero-text{font-size:13px;line-height:20px;width:440px;margin-top:14px;color:#eee}
.hero-btn{display:inline-block;margin-top:20px;border:1px solid var(--orange);color:var(--orange);font-size:11px;padding:10px 13px}
.hero-arrow{position:absolute;top:231px;width:26px;height:26px;border:1px solid #888;border-radius:50%;display:flex;align-items:center;justify-content:center}
.hero-arrow.prev{left:16px}
.hero-arrow.next{right:16px}

/* welcome */
.welcome{height:329px;background:var(--light-bg);text-align:center;padding-top:45px}
.welcome h1{font-size:22px;font-weight:700}
.welcome .intro{width:680px;margin:16px auto 0;font-size:11.5px;line-height:19px;color:#555}
.features{display:flex;justify-content:center;margin-top:42px}
.feature{width:328px}
.feature .icon{width:60px;height:60px;border-radius:50%;background:#cfcfcf;margin:0 auto;display:flex;align-items:center;justify-content:center}
.feature h3{font-size:13px;font-weight:700;margin-top:15px}
.feature p{font-size:11px;color:#666;margin-top:5px}

/* tabs */
.product-tabs{position:absolute;top:1055px;left:111px;width:978px;border-bottom:1px solid var(--line);display:flex;justify-content:center;gap:44px;font-family:"Montserrat",Arial,sans-serif;font-size:11px;font-weight:600;height:25px}
.product-tabs .tab{padding-top:4px}
.product-tabs .active{color:var(--orange);border-bottom:2px solid var(--orange)}

/* product grid */
.product-grid{position:absolute;left:111px;width:978px;display:flex;gap:27px}
.product-card{width:224px;height:300px;border:1px solid var(--line);position:relative;text-align:center;background:var(--white)}
.badge{position:absolute;left:0;top:18px;color:var(--white);font-size:10px;font-weight:600;padding:6px 12px;font-family:"Montserrat",Arial,sans-serif;z-index:1}
.badge.new{background:var(--teal)}
.badge.sale{background:var(--orange)}
.product-photo{width:190px;height:120px;margin:16px auto 0}
.photo-bike{background:linear-gradient(160deg,#f6f7fc 0%,#dfe3f4 55%,#c7cdea 100%)}
.photo-bag{background:linear-gradient(160deg,#faf6f1 0%,#eadccd 55%,#d8c0a6 100%)}
.photo-rod{background:linear-gradient(160deg,#fafafa 0%,#ececec 55%,#d9d9d9 100%)}
.rating{display:flex;align-items:center;justify-content:center;gap:8px;margin-top:18px}
.rating i{display:block;height:1px;width:34px;background:var(--line)}
.rating svg{display:block}
.product-card h4{font-family:"Montserrat",Arial,sans-serif;font-size:11.5px;font-weight:700;margin-top:12px}
.product-card .desc{font-size:10.5px;color:var(--muted);line-height:16px;margin-top:6px}
.product-card .price{font-family:"Montserrat",Arial,sans-serif;color:var(--orange);font-weight:700;font-size:13.5px;margin-top:12px}

/* promo banners */
.promo-row{position:absolute;top:1432px;left:111px;width:978px;display:flex;justify-content:space-between}
.promo{width:471px;height:215px;display:flex;align-items:center;justify-content:center}
.promo-equipment{background:linear-gradient(135deg,#3b3626,#5a5440 45%,#2b2a22)}
.promo-fear{background:linear-gradient(135deg,#4a4636,#6a6450 50%,#3a3628)}
.promo span{border:2px solid #ddd;color:var(--white);font-size:17px;font-weight:600;padding:10px 32px;text-transform:uppercase;background:rgba(0,0,0,.25)}

/* featured */
.featured-title{position:absolute;top:1686px;left:111px;width:978px;font-size:22px;font-weight:700;padding-bottom:8px;border-bottom:5px solid #d4d4d4}

/* newsletter */
.newsletter{position:absolute;top:2111px;left:0;width:1200px;height:108px;background:var(--orange);color:var(--white)}
.newsletter .copy{position:absolute;left:111px;top:30px;width:290px}
.newsletter h2{font-size:19px;font-weight:600;white-space:nowrap}
.newsletter p{font-size:12px;margin-top:3px}
.newsletter .field{position:absolute;left:420px;top:35px;width:239px;height:38px;background:var(--white);color:#999;font-size:11.5px;padding:11px 12px}
.newsletter .subscribe{position:absolute;left:674px;top:35px;width:107px;height:38px;background:var(--black);color:var(--white);font-family:"Montserrat",Arial,sans-serif;font-size:14px;font-weight:600;text-align:center;line-height:38px}
.social{position:absolute;left:866px;top:32px;display:flex;gap:15px}
.social a{width:44px;height:44px;border:2px solid var(--white);border-radius:50%;display:flex;align-items:center;justify-content:center;font-size:11px;font-weight:600}

/* footer */
.site-footer{position:absolute;top:2219px;left:0;width:1200px;height:276px;background:var(--black);color:#ddd}
.footer-brand{position:absolute;left:111px;top:34px;font-family:"Montserrat",Arial,sans-serif;font-weight:800;font-size:24px;color:var(--orange);display:flex;align-items:center;gap:8px}
.footer-brand .mark{width:12px;height:12px;background:var(--orange)}
.contact{position:absolute;left:111px;top:92px}
.contact li{list-style:none;display:flex;align-items:center;gap:14px;font-size:12px;margin-bottom:20px;line-height:16px}
.contact .ci{width:30px;height:30px;border-radius:50%;border:1px solid #555;display:flex;align-items:center;justify-content:center;flex-shrink:0}
.contact .ci.pin{background:var(--orange);border-color:var(--orange)}
.footer-col{position:absolute;top:82px}
.footer-col h5{font-family:"Montserrat",Arial,sans-serif;color:var(--orange);font-size:16px;font-weight:700;margin-bottom:18px}
.footer-col li{list-style:none;font-size:11.5px;line-height:22px}
.footer-col p{font-size:11.5px;line-height:19px;width:255px}
.footer-col .more{color:var(--orange);font-size:11px;font-weight:600;margin-top:8px;display:block}

/* bottom bar */
.bottom-bar{position:absolute;top:2495px;left:0;width:1200px;height:65px;background:var(--black);border-top:1px solid #222;color:#ccc;font-size:11px}
.bottom-bar .copyright{position:absolute;left:111px;top:24px}
.payments{position:absolute;right:111px;top:17px;display:flex;gap:8px}
.payments span{width:52px;height:32px;background:var(--white);border-radius:3px;color:var(--dark-text);font-family:"Montserrat",Arial,sans-serif;font-size:10px;font-weight:700;display:flex;align-items:center;justify-content:center}
</style>
</head>
<body>

<svg class="icon-defs" aria-hidden="true"><defs><path id="star" d="M7 0l2 5h5l-4 3 2 5-5-3-5 3 2-5-4-3h5z"/></defs></svg>

<div class="top-bar">
  <a href="#">Log in</a><a href="#">Register</a><a href="#">My Account</a><a href="#">Wishlist</a><a href="#">Checkout</a>
  <span class="currency">Currency: <b>USD ▾</b></span>
</div>

<header class="site-header">
  <div class="brand"><span class="mark"></span>RIDGEMANTIS</div>
  <div class="cart-box">ITEM (0)<span class="total">0.00</span>
    <svg width="22" height="20" viewBox="0 0 22 20"><path d="M1 2h4l3 10h10l3-7H7" fill="none" stroke="#ff6a00" stroke-width="2"/><circle cx="9" cy="16" r="2" fill="#ff6a00"/><circle cx="17" cy="16" r="2" fill="#ff6a00"/></svg>
  </div>
</header>

<nav class="main-nav">
  <a href="#">HOME</a><a href="#">BEST SELLER</a><a href="#">NEW PRODUCTS</a><a href="#">BLOG</a><a href="#">CONTACT US</a><a href="#">ABOUT US</a>
</nav>

<section class="hero">
  <div class="hero-photo" role="img" aria-label="Hunter in camouflage kneeling with binoculars against a sunset sky"></div>
  <div class="hero-copy">
    <h2 class="hero-title heading">Outdoor<span>Accessories</span></h2>
    <p class="hero-text">Dorem ipsum dolor sit amet, consectetuer adipiscing elit, sed diam nonummy nibh euismod tincidunt.</p>
    <a class="hero-btn" href="#">SHOPPING NOW</a>
  </div>
  <span class="hero-arrow prev"><svg width="10" height="10" viewBox="0 0 10 10"><path d="M7 1L3 5l4 4" fill="none" stroke="#aaa" stroke-width="1.5"/></svg></span>
  <span class="hero-arrow next"><svg width="10" height="10" viewBox="0 0 10 10"><path d="M3 1l4 4-4 4" fill="none" stroke="#aaa" stroke-width="1.5"/></svg></span>
</section>

<section class="welcome">
  <h1 class="heading">WELCOME TO OUR STORE</h1>
  <p class="intro">Lorem ipsum dolor sit amet, consectetuer adipiscing elit, sed diam nonummy nibh euismod tincidunt ut laoreet dolore magn aliquam erat volutpat. Ut wisi enim ad minim veniam, quis nostrud exerci tation ullamcorper suscipit lobortis nisl ut aliquip ex ea commodo consequat. Duis autem vel eum iriure dolor in hendrerit</p>
  <div class="features">
    <div class="feature">
      <div class="icon"><svg width="30" height="20" viewBox="0 0 30 20"><rect x="1" y="3" width="17" height="11" fill="#111"/><path d="M18 6h6l4 4v4H18z" fill="#111"/><circle cx="7" cy="16" r="3" fill="#111"/><circle cx="23" cy="16" r="3" fill="#111"/></svg></div>
      <h3 class="heading">FREE SHIPPING</h3><p>Dolor sit amet, consectetuer adipiscing elit</p>
    </div>
    <div class="feature">
      <div class="icon"><svg width="16" height="28" viewBox="0 0 16 28"><text x="8" y="22" font-family="Montserrat,sans-serif" font-size="24" font-weight="700" text-anchor="middle" fill="#111">$</text></svg></div>
      <h3 class="heading">MONEY BACK GUARNTEE</h3><p>Dolor sit amet, consectetuer adipiscing elit</p>
    </div>
    <div class="feature">
      <div class="icon"><svg width="22" height="22" viewBox="0 0 22 22"><path d="M5 3l4 4-2 2c1 3 3 5 6 6l2-2 4 4-2 3C10 20 2 12 2 5z" fill="#111"/><path d="M13 3a6 6 0 0 1 6 6M13 6a3 3 0 0 1 3 3" fill="none" stroke="#111" stroke-width="1.5"/></svg></div>
      <h3 class="heading">24/7 CUSTOMER SERVICE</h3><p>Dolor sit amet, consectetuer adipiscing elit</p>
    </div>
  </div>
</section>

<div class="product-tabs">
  <span class="tab active">BEST SELLER PRODUCTS</span><span class="tab">MOST VIEWED PRODUCTS</span><span class="tab">NEW PRODUCTS</span>
</div>

<div class="product-grid" style="top:1108px">
  <article class="product-card"><span class="badge new">NEW</span><div class="product-photo photo-bike" role="img" aria-label="Blue motocross dirt bike"></div>
    <div class="rating"><i></i><svg width="80" height="14" viewBox="0 0 80 14"><g fill="#f5b400"><use href="#star"/><use href="#star" x="16"/><use href="#star" x="32"/></g><g fill="#d0d0d0"><use href="#star" x="48"/><use href="#star" x="64"/></g></svg><i></i></div>
    <h4>MX DIRT BIKE RIDING</h4><p class="desc">There are many variations assages<br>of Lorem Ipsum</p><p class="price">AUD 70.00</p></article>
  <article class="product-card"><span class="badge new">NEW</span><div class="product-photo photo-bag" role="img" aria-label="Brown leather shoulder bag"></div>
    <div class="rating"><i></i><svg width="80" height="14" viewBox="0 0 80 14"><g fill="#f5b400"><use href="#star"/><use href="#star" x="16"/><use href="#star" x="32"/></g><g fill="#d0d0d0"><use href="#star" x="48"/><use href="#star" x="64"/></g></svg><i></i></div>
    <h4>MX DIRT BIKE RIDING</h4><p class="desc">There are many variations assages<br>of Lorem Ipsum</p><p class="price">AUD 70.00</p></article>
  <article class="product-card"><span class="badge sale">SALE</span><div class="product-photo photo-rod" role="img" aria-label="Pair of fishing rods with reels"></div>
    <div class="rating"><i></i><svg width="80" height="14" viewBox="0 0 80 14"><g fill="#f5b400"><use href="#star"/><use href="#star" x="16"/><use href="#star" x="32"/></g><g fill="#d0d0d0"><use href="#star" x="48"/><use href="#star" x="64"/></g></svg><i></i></div>
    <h4>MX DIRT BIKE RIDING</h4><p class="desc">There are many variations assages<br>of Lorem Ipsum</p><p class="price">AUD 70.00</p></article>
  <article class="product-card"><span class="badge new">NEW</span><div class="product-photo photo-bag" role="img" aria-label="Brown leather shoulder bag"></div>
    <div class="rating"><i></i><svg width="80" height="14" viewBox="0 0 80 14"><g fill="#f5b400"><use href="#star"/><use href="#star" x="16"/><use href="#star" x="32"/></g><g fill="#d0d0d0"><use href="#star" x="48"/><use href="#star" x="64"/></g></svg><i></i></div>
    <h4>MX DIRT BIKE RIDING</h4><p class="desc">There are many variations assages<br>of Lorem Ipsum</p><p class="price">AUD 70.00</p></article>
</div>

<div class="promo-row">
  <a class="promo promo-equipment" href="#" role="img" aria-label="Camouflaged hunting gear resting on the ground"><span>EQUIPMENT</span></a>
  <a class="promo promo-fear" href="#" role="img" aria-label="Burrow entrance in rough forest ground"><span>DON'T LET FEAR STOP YOU</span></a>
</div>

<h2 class="featured-title heading">FEATURED PRODUCTS</h2>

<div class="product-grid" style="top:1741px">
  <article class="product-card"><span class="badge new">NEW</span><div class="product-photo photo-bike" role="img" aria-label="Blue motocross dirt bike"></div>
    <div class="rating"><i></i><svg width="80" height="14" viewBox="0 0 80 14"><g fill="#f5b400"><use href="#star"/><use href="#star" x="16"/><use href="#star" x="32"/></g><g fill="#d0d0d0"><use href="#star" x="48"/><use href="#star" x="64"/></g></svg><i></i></div>
    <h4>MX DIRT BIKE RIDING</h4><p class="desc">There are many variations assages<br>of Lorem Ipsum</p><p class="price">AUD 70.00</p></article>
  <article class="product-card"><span class="badge new">NEW</span><div class="product-photo photo-bag" role="img" aria-label="Brown leather shoulder bag"></div>
    <div class="rating"><i></i><svg width="80" height="14" viewBox="0 0 80 14"><g fill="#f5b400"><use href="#star"/><use href="#star" x="16"/><use href="#star" x="32"/></g><g fill="#d0d0d0"><use href="#star" x="48"/><use href="#star" x="64"/></g></svg><i></i></div>
    <h4>MX DIRT BIKE RIDING</h4><p class="desc">There are many variations assages<br>of Lorem Ipsum</p><p class="price">AUD 70.00</p></article>
  <article class="product-card"><span class="badge sale">SALE</span><div class="product-photo photo-rod" role="img" aria-label="Pair of fishing rods with reels"></div>
    <div class="rating"><i></i><svg width="80" height="14" viewBox="0 0 80 14"><g fill="#f5b400"><use href="#star"/><use href="#star" x="16"/><use href="#star" x="32"/></g><g fill="#d0d0d0"><use href="#star" x="48"/><use href="#star" x="64"/></g></svg><i></i></div>
    <h4>MX DIRT BIKE RIDING</h4><p class="desc">There are many variations assages<br>of Lorem Ipsum</p><p class="price">AUD 70.00</p></article>
  <article class="product-card"><span class="badge new">NEW</span><div class="product-photo photo-bag" role="img" aria-label="Brown leather shoulder bag"></div>
    <div class="rating"><i></i><svg width="80" height="14" viewBox="0 0 80 14"><g fill="#f5b400"><use href="#star"/><use href="#star" x="16"/><use href="#star" x="32"/></g><g fill="#d0d0d0"><use href="#star" x="48"/><use href="#star" x="64"/></g></svg><i></i></div>
    <h4>MX DIRT BIKE RIDING</h4><p class="desc">There are many variations assages<br>of Lorem Ipsum</p><p class="price">AUD 70.00</p></article>
</div>

<section class="newsletter">
  <div class="copy"><h2 class="heading">SIGNUP FOR NEWSLETTER</h2><p>Incarcatoare Universale Incarcatoare</p></div>
  <div class="field">Enter Your Mail ID</div>
  <div class="subscribe">SUBSCRIBE</div>
  <div class="social">
    <a href="#" title="Campfeed">CF</a><a href="#" title="Chirper">CH</a><a href="#" title="Circlo">CI</a><a href="#" title="Snapgrid">SG</a>
  </div>
</section>

<footer class="site-footer">
  <div class="footer-brand"><span class="mark"></span>RIDGEMANTIS</div>
  <ul class="contact">
    <li><span class="ci pin"><svg width="12" height="16" viewBox="0 0 12 16"><path d="M6 0a6 6 0 0 0-6 6c0 4 6 10 6 10s6-6 6-10a6 6 0 0 0-6-6z" fill="#fff"/><circle cx="6" cy="6" r="2" fill="#ff6a00"/></svg></span>12 Ridgeline Road, Bendigo<br>VIC 3550</li>
    <li><span class="ci"><svg width="14" height="14" viewBox="0 0 22 22"><path d="M5 3l4 4-2 2c1 3 3 5 6 6l2-2 4 4-2 3C10 20 2 12 2 5z" fill="#ff6a00"/></svg></span>0400 555 019</li>
    <li><span class="ci"><svg width="14" height="10" viewBox="0 0 14 10"><rect x="0.5" y="0.5" width="13" height="9" fill="none" stroke="#ff6a00"/><path d="M1 1l6 5 6-5" fill="none" stroke="#ff6a00"/></svg></span>hello@ridgemantis.com.au</li>
  </ul>
  <div class="footer-col" style="left:398px"><h5>MY ACCOUNT</h5><ul><li>My Order</li><li>Order History</li><li>My Wishlist</li><li>My Addresses</li><li>Advanced Search</li><li>My Credit Slips</li></ul></div>
  <div class="footer-col" style="left:621px"><h5>OUR SERVICES</h5><ul><li>Home</li><li>Best Seller</li><li>New Products</li><li>Blog</li><li>Contact Us</li><li>About Us</li></ul></div>
  <div class="footer-col" style="left:836px"><h5>ABOUT US</h5><p>There are many variations of passages of Lorem Ipsum available, but the majority have suffered alteration in some form, by injected humour, or rndomised words which don't look even slightly believable. If you are going.</p><a class="more" href="#">MORE »</a></div>
</footer>

<div class="bottom-bar">
  <span class="copyright">© All Rights Reserved 2017.</span>
  <div class="payments"><span>Paywell</span><span>Cardia</span><span>Findly</span><span>Vexa</span></div>
</div>

</body>
</html>
```